Business card design needed

www.marlonfab.com.au
Our primary services:
On-site welding.
On-site industrial maintenance.
On-site repairs and capital works projects specialising in pipe fabrication.
Our ability to work on-site with our dedicated mobile equipment is essential to our capability to provide a quality maintenance service to our customers. We are capable of providing a full team of qualified boilermakers that can work either to your plan or project manage if a plan has not been developed.
Industry/Entity Type
Industrial
Contact Information for Business Card
company name- MARLON FAB PTY LTD
story - industrial steel fabrication, constructions and pipelines
Director - Greg Hadley
workshop address - shed 7, 3862 kemble rd Tully
postal address - P.O BOX 628 TULLY Q 4854
mobile - 0429385106
w/shop phone - 0752937048
fax - 0752938159
email - admin@marlonfab.com.au
web - www.marlonfab.com.au
Logo Text
MARLON FAB pty ltd
Look and feel

```html
<!DOCTYPE html>
<html lang="en">
<head>
<meta charset="utf-8">
<title>Marlon Fab – Business Card</title>
<link rel="stylesheet" href="https://fonts.googleapis.com/css2?family=Arimo:ital,wght@0,400;0,700;1,400&display=swap">
<style>
  :root {
    --brand-blue: #233f93;
    --ink: #1a1a1a;
    --paper: #ffffff;
    --steel-dark: #8a8a8a;
    --steel-mid: #b4b4b4;
    --steel-light: #d6d6d6;
    --edge: #6f6f6f;
  }
  * { margin: 0; padding: 0; box-sizing: border-box; }
  html, body {
    width: 1200px; height: 1200px; overflow: hidden;
    background: var(--paper);
    font-family: "Arimo", Arial, sans-serif;
  }
  .canvas { position: relative; width: 1200px; height: 1200px; }

  .card {
    position: absolute; left: 204px; width: 792px; height: 457px;
    border: 1px solid var(--edge);
    box-shadow: 6px 8px 14px rgba(0,0,0,0.22);
    overflow: hidden;
    background: var(--paper);
  }
  .card--front { top: 82px; }
  .card--back { top: 633px; }

  .steel-plate {
    position: absolute; inset: 0;
    background:
      linear-gradient(100deg, transparent 20%, rgba(255,255,255,0.28) 38%, transparent 55%),
      linear-gradient(160deg, var(--steel-light) 0%, var(--steel-mid) 35%, var(--steel-dark) 70%, var(--steel-mid) 100%);
  }
  .card--front .steel-plate {
    clip-path: polygon(0 0, 433px 0, 296px 100%, 0 100%);
  }
  .accent-band { position: absolute; inset: 0; width: 100%; height: 100%; }

  .wordmark {
    position: absolute; display: flex; align-items: center;
    color: var(--brand-blue); font-weight: 400; white-space: nowrap;
  }
  .wordmark__square { background: var(--brand-blue); flex: none; }
  .card--front .wordmark { left: 66px; top: 168px; font-size: 33px; gap: 10px; }
  .card--front .wordmark__square { width: 24px; height: 24px; }
  .card--back .wordmark { left: 50%; top: 50%; transform: translate(-50%, -50%); font-size: 50px; gap: 14px; }
  .card--back .wordmark__square { width: 36px; height: 36px; }

  .tagline {
    position: absolute; left: 52px; top: 263px; width: 268px;
    text-align: center; color: var(--brand-blue);
    font-style: italic; font-size: 17px; line-height: 23px;
  }

  .person { position: absolute; right: 34px; top: 77px; text-align: right; }
  .person__name { color: var(--brand-blue); font-weight: 700; font-size: 24px; line-height: 28px; }
  .person__title { color: var(--ink); font-size: 20px; line-height: 24px; }

  .address {
    position: absolute; right: 34px; top: 186px; text-align: right;
    font-style: normal; color: var(--ink); font-size: 20px; line-height: 26px;
  }

  .contacts {
    position: absolute; left: 470px; right: 34px; top: 297px;
    color: var(--ink); font-size: 20px; line-height: 26px; list-style: none;
  }
  .contacts__row { position: relative; text-align: right; }
  .contacts__label {
    position: absolute; top: 0; color: var(--brand-blue); font-weight: 700;
  }
  .contacts__label--phone { left: 112px; }
  .contacts__label--web { left: 2px; }
</style>
</head>
<body>
<main class="canvas">

  <section class="card card--front" aria-label="Business card front">
    <div class="steel-plate" role="img" aria-label="Brushed steel checker plate texture"></div>
    <svg class="accent-band" viewBox="0 0 792 457" preserveAspectRatio="none" aria-hidden="true">
      <polygon points="433,0 455,0 320,457 296,457" fill="var(--brand-blue)"/>
    </svg>

    <div class="wordmark"><span class="wordmark__square"></span>MARLON FAB</div>
    <p class="tagline">Industrial steel fabrication, constructions and pipelines</p>

    <div class="person">
      <p class="person__name">Greg Hadley</p>
      <p class="person__title">DIRECTOR</p>
    </div>

    <address class="address">
      Shed 7, 3862 Kemble Rd<br>
      (PO BOX 628)<br>
      KELLAVALE QLD 4861
    </address>

    <ul class="contacts">
      <li class="contacts__row"><span class="contacts__label contacts__label--phone">M</span>0429 385 106</li>
      <li class="contacts__row"><span class="contacts__label contacts__label--phone">P</span>07 5293 7048</li>
      <li class="contacts__row"><span class="contacts__label contacts__label--phone">F</span>07 5293 8159</li>
      <li class="contacts__row"><span class="contacts__label contacts__label--web">E</span>admin@marlonfab.com.au</li>
      <li class="contacts__row"><span class="contacts__label contacts__label--web">W</span>www.marlonfab.com.au</li>
    </ul>
  </section>

  <section class="card card--back" aria-label="Business card back">
    <div class="steel-plate" role="img" aria-label="Brushed steel checker plate texture"></div>
    <div class="wordmark"><span class="wordmark__square"></span>MARLON FAB</div>
  </section>

</main>
</body>
</html>
```